Educational clinic needs a new webpage design

I have a relatively new website but I am unhappy with the design. I was hoping the look of it would more match my logo, brochures, business cards, and postcards. The content is good and it's already mobile ready. The designer used square space, which I would like to keep if possible. My website is www.willowgatestudio.com

Target Market(s)

Parents of school age children

Industry/Entity Type

Education

Number of Pages Required

5+ page

Requirements
Must have
• Pictures must depict the diversity of our students. We service all ages, from preschool through college and our students come from varying races.
Should not have
• I try to avoid the word "tutoring" because what we do is so much more. I like the tag line of "results that go beyond traditional tutoring"

```html
<!DOCTYPE html>
<html lang="en">
<head>
<meta charset="utf-8">
<title>Willowgate Studio</title>
<link rel="stylesheet" href="https://fonts.googleapis.com/css2?family=Jost:wght@500;600;700&family=Open+Sans:wght@400;600;700&display=swap">
<style>
:root{
  --purple:#6b2c91;
  --purple-dark:#55207a;
  --green:#8dc63f;
  --ink:#1e1e1e;
  --muted:#777;
  --card:#f4f4f4;
  --navy:#263244;
  --navy-deep:#1c2230;
  --line:#e2e2e2;
}
*{box-sizing:border-box;margin:0;padding:0}
html,body{width:1200px;height:3352px;overflow:hidden}
body{font-family:"Open Sans",sans-serif;color:var(--ink);background:#fff;position:relative}
.abs{position:absolute}
.topbar{left:0;top:0;width:1200px;height:34px;background:#000}
.topbar .social{position:absolute;right:40px;top:10px;display:flex;gap:12px}
.topbar .social span{width:13px;height:13px;border-radius:50%;background:#fff;display:block}
.brand{left:49px;top:46px;height:60px;display:flex;align-items:center;gap:14px}
.brand .mark{width:60px;height:60px;border-radius:50%;background:var(--purple)}
.brand .name{font-family:"Jost",sans-serif;font-weight:700;font-size:34px;color:var(--purple);line-height:1}
.email{left:552px;top:66px;display:flex;align-items:center;gap:20px}
.email .icon{width:42px;height:42px;background:var(--purple);display:flex;align-items:center;justify-content:center}
.email small{display:block;font-size:12px;color:#333}
.email strong{font-size:15px;font-weight:600;color:#222}
.btn-outline,.btn-solid{font-size:13px;font-weight:600;text-transform:uppercase;display:flex;align-items:center;justify-content:center;gap:8px;height:33px}
.btn-outline{left:869px;top:72px;width:132px;border:2px solid var(--purple);color:var(--purple)}
.btn-solid{left:1048px;top:72px;width:105px;background:var(--purple);color:#fff}
.nav{left:47px;top:141px;width:1106px;height:42px;background:var(--purple);display:flex;align-items:center;padding-left:40px}
.nav a{color:#fff;text-decoration:none;font-size:14px;padding:0 28px;border-right:1px solid rgba(255,255,255,.7);line-height:16px}
.nav a:first-child{padding-left:0}
.nav a:last-of-type{border:none}
.roll{left:894px;top:141px;width:214px;height:42px;background:var(--green);clip-path:polygon(22px 0,100% 0,100% 100%,0 100%);color:#2a2a2a;font-size:14px;display:flex;align-items:center;justify-content:center}
.go{left:1108px;top:141px;width:45px;height:42px;background:var(--purple-dark);color:#fff;font-size:14px;display:flex;align-items:center;justify-content:center}
.hero{left:0;top:183px;width:1200px;height:525px;background:linear-gradient(110deg,#c9a078 0%,#e8d6c4 28%,#b9b3ad 55%,#7d6d68 80%,#c58a55 100%)}
.hero h1{position:absolute;left:0;width:100%;top:300px;text-align:center;color:#fff;font-family:"Jost",sans-serif;font-weight:700;font-size:46px;line-height:54px;letter-spacing:1px;text-transform:uppercase}
.hero .more{position:absolute;left:507px;top:420px;width:186px;height:41px;border:2px solid #fff;outline:2px solid #fff;outline-offset:-6px;background:#fff;color:var(--purple);font-size:15px;font-weight:600;display:flex;align-items:center;justify-content:center}
.hero .dots{position:absolute;top:480px;left:0;width:100%;display:flex;justify-content:center;gap:18px}
.hero .dots span{width:11px;height:11px;border-radius:50%;background:#fff}
.hero .dots span.on{background:var(--green)}
.section-title{left:0;width:1200px;text-align:center;font-family:"Jost",sans-serif;font-weight:600;font-size:36px;letter-spacing:1px}
.intro{left:210px;top:828px;width:780px;text-align:center;font-size:14px;line-height:28px;color:#555}
.btn{background:var(--purple);color:#fff;font-size:13px;font-weight:700;text-transform:uppercase;display:flex;align-items:center;justify-content:center;border-bottom:3px solid var(--purple-dark)}
.subtitle{left:0;width:1200px;top:1086px;text-align:center;font-size:14px;color:#777}
.divider{left:450px;top:1129px;width:300px;height:1px;background:var(--line)}
.card{top:1187px;width:331px;height:485px;background:var(--card)}
.card .photo{height:199px;border-bottom:3px solid #6fa6d6}
.card .meta{position:absolute;left:32px;top:238px;font-size:10px;color:#777;display:flex;gap:20px;text-transform:uppercase}
.card .meta b{color:var(--purple);font-weight:600}
.card h3{position:absolute;left:32px;top:290px;font-size:12px;font-weight:700;text-transform:uppercase;letter-spacing:.3px}
.card p{position:absolute;left:32px;top:334px;width:270px;font-size:11.5px;line-height:22px;color:#555}
.card .btn{position:absolute;left:32px;top:427px;width:95px;height:32px;font-size:11px}
.gallery{left:47px;top:1833px;width:1106px;height:634px;display:grid;grid-template-columns:repeat(4,1fr);grid-template-rows:205px 210px 1fr;gap:10px}
.gallery div{position:relative}
.g-a{grid-column:1;grid-row:1;background:linear-gradient(135deg,#8a4fb0,#6b2c91)}
.g-a .plus{position:absolute;left:50%;top:50%;width:64px;height:64px;margin:-32px;border-radius:50%;background:var(--green);display:flex;align-items:center;justify-content:center}
.g-b{grid-column:2/4;grid-row:1;background:linear-gradient(100deg,#5b4a45,#8b6c5c,#c9a892)}
.g-c{grid-column:4;grid-row:1;background:linear-gradient(120deg,#d9c7b7,#6b3e8e 70%)}
.g-d{grid-column:1;grid-row:2;background:linear-gradient(120deg,#7d7d7d,#444)}
.g-e{grid-column:2;grid-row:2/4;background:linear-gradient(180deg,#2f3b3a,#6a7270 50%,#b83a2e 85%)}
.g-f{grid-column:3/5;grid-row:2/4;background:linear-gradient(110deg,#e0d2c8,#a9b4c0 50%,#7b4aa0 85%)}
.g-g{grid-column:1;grid-row:3;background:linear-gradient(120deg,#555,#a49a90)}
.contact{left:0;top:2494px;width:1200px;height:434px;background:var(--navy)}
.contact-deep{left:0;top:2928px;width:1200px;height:424px;background:var(--navy-deep)}
.contact h2{position:absolute;top:18px;left:0;width:100%;text-align:center;color:#fff;font-family:"Jost",sans-serif;font-weight:600;font-size:34px}
.contact .bar{position:absolute;left:585px;top:76px;width:30px;height:4px;background:var(--green)}
.info{position:absolute;top:130px;width:300px;text-align:center;color:#8a94a3;font-size:14px;line-height:22px}
.info .ring{width:76px;height:76px;border:1px solid #3e4a5c;border-radius:50%;margin:0 auto 28px;display:flex;align-items:center;justify-content:center}
.query{left:47px;top:2885px;width:1106px;height:389px;background:#fff}
.query h2{position:absolute;top:32px;left:0;width:100%;text-align:center;font-family:"Jost",sans-serif;font-weight:600;font-size:34px}
.field{position:absolute;background:#f2f2f2;font-size:11px;color:#888;padding:10px 18px}
.query .btn{position:absolute;left:460px;top:300px;width:159px;height:47px;font-size:15px;letter-spacing:1px}
.footer{left:57px;top:3312px;font-size:12px;color:#8a94a3}
.pay{left:1022px;top:3298px;display:flex;flex-direction:column;align-items:center;gap:4px}
.pay .pill{width:100px;height:22px;border-radius:11px;background:#f4b223;color:#1e2a55;font-size:11px;font-weight:700;display:flex;align-items:center;justify-content:center}
.pay .cards{display:flex;gap:3px}
.pay .cards span{width:22px;height:12px;background:#ccd3dc;border-radius:2px}
</style>
</head>
<body>

<div class="abs topbar"><div class="social"><span></span><span></span><span></span><span></span><span></span><span></span></div></div>

<div class="abs brand">
  <div class="mark"></div>
  <div class="name">Willowgate Studio</div>
</div>

<div class="abs email">
  <div class="icon"><svg width="20" height="16" viewBox="0 0 20 16"><rect x="1" y="1" width="18" height="14" fill="none" stroke="#fff" stroke-width="2"/><path d="M1 1l9 8 9-8" fill="none" stroke="#fff" stroke-width="2"/></svg></div>
  <div><small>Email Contact</small><strong>info@willowgatestudio.com</strong></div>
</div>
<div class="abs btn-outline"><svg width="11" height="13" viewBox="0 0 11 13"><rect x="0" y="5" width="11" height="8" fill="#6b2c91"/><path d="M2.5 5V3.5a3 3 0 016 0V5" fill="none" stroke="#6b2c91" stroke-width="1.6"/></svg>Log Up</div>
<div class="abs btn-solid"><svg width="11" height="13" viewBox="0 0 11 13"><rect x="0" y="5" width="11" height="8" fill="#fff"/><path d="M2.5 5V3.5a3 3 0 016 0V5" fill="none" stroke="#fff" stroke-width="1.6"/></svg>Sign Up</div>

<nav class="abs nav"><a>Home</a><a>Services</a><a>About Us</a><a>Blog</a><a>Payments</a><a>Contact us</a></nav>
<div class="abs roll">Enter Roll Number</div>
<div class="abs go">GO</div>

<section class="abs hero" role="img" aria-label="Smiling students studying together in a classroom">
  <h1>Take the first step<br>to knowledge with us</h1>
  <div class="more">Read More About</div>
  <div class="dots"><span></span><span class="on"></span><span></span></div>
</section>

<h2 class="abs section-title" style="top:762px">What We Do</h2>
<p class="abs intro">Since 2004, we have been helping families with their educational needs. We are more than passionate about students' success. At Willowgate Studio you'll find a welcoming environment, kind smiles and highly trained Learning Skills Specialists. Students will find a place where they will always be successful!</p>
<div class="abs btn" style="left:536px;top:945px;width:130px;height:38px">Read More</div>

<h2 class="abs section-title" style="top:1032px">Online Education News</h2>
<p class="abs subtitle">Having over 9 million students worldwide and more than 50,000 online courses available.</p>
<div class="abs divider"></div>

<article class="abs card" style="left:47px">
  <div class="photo" role="img" aria-label="Students working at computers in a bright office" style="background:linear-gradient(160deg,#dfe4ea,#8e9aa8)"></div>
  <div class="meta"><span>By <b>Admin</b></span><span>January 3, 2016</span></div>
  <h3>Becoming a Better Developer</h3>
  <p>The most common thought is that coding whether it be as a software developer or a web developer can be improve through the use of tools.</p>
  <div class="btn">Read More</div>
</article>
<article class="abs card" style="left:434px">
  <div class="photo" role="img" aria-label="Team of young people planning around a table" style="background:linear-gradient(160deg,#e8d9cc,#c44d6a 60%,#7a5c8a)"></div>
  <div class="meta"><span>By <b>Admin</b></span><span>January 6, 2016</span></div>
  <h3>Customers and Competitors</h3>
  <p>A successful business relies heavily on people and networking. A good team and wider network is essential to success and growth.</p>
  <div class="btn">Read More</div>
</article>
<article class="abs card" style="left:822px">
  <div class="photo" role="img" aria-label="Hands drawing with coloured pencils on paper" style="background:linear-gradient(160deg,#b0563f,#e2d7cc 60%,#d2b49b)"></div>
  <div class="meta"><span>By <b>Admin</b></span><span>January 9, 2016</span></div>
  <h3>Learning and Collobarating</h3>
  <p>You are probably used to learning online on a daily basis, including turning to your phone for information rather than referring to books.</p>
  <div class="btn">Read More</div>
</article>

<h2 class="abs section-title" style="top:1712px">Photo Gallery</h2>
<div class="abs gallery">
  <div class="g-a" role="img" aria-label="Students reading together, purple overlay"><div class="plus"><svg width="26" height="26" viewBox="0 0 26 26"><path d="M13 3v20M3 13h20" stroke="#1e1e1e" stroke-width="4"/></svg></div></div>
  <div class="g-b" role="img" aria-label="Students seated in a lecture hall"></div>
  <div class="g-c" role="img" aria-label="Student smiling beside library shelves"></div>
  <div class="g-d" role="img" aria-label="Students with phones in front of a chalkboard"></div>
  <div class="g-e" role="img" aria-label="Stack of books with an apple before a chalkboard"></div>
  <div class="g-f" role="img" aria-label="Two students sharing a tablet at a table"></div>
  <div class="g-g" role="img" aria-label="Graduate with a laptop and books"></div>
</div>

<section class="abs contact">
  <h2>Contact Information</h2>
  <div class="bar"></div>
  <div class="info" style="left:49px">
    <div class="ring"><svg width="16" height="22" viewBox="0 0 16 22"><path d="M8 0a8 8 0 00-8 8c0 6 8 14 8 14s8-8 8-14a8 8 0 00-8-8z" fill="#fff"/><circle cx="8" cy="8" r="3" fill="#263244"/></svg></div>
    Willowgate Studio,<br>418 Maple Hollow Road,<br>Brookfield, IL
  </div>
  <div class="info" style="left:449px">
    <div class="ring"><svg width="20" height="20" viewBox="0 0 20 20"><path d="M4 1l4 4-2 3c1 3 3 5 6 6l3-2 4 4-3 3C8 19 1 12 1 4z" fill="#fff"/></svg></div>
    60513<br>555-014-2290
  </div>
  <div class="info" style="left:818px">
    <div class="ring"><svg width="20" height="16" viewBox="0 0 20 16"><rect x="1" y="1" width="18" height="14" rx="2" fill="none" stroke="#fff" stroke-width="2"/><path d="M1 2l9 7 9-7" fill="none" stroke="#fff" stroke-width="2"/></svg></div>
    info@willowgatestudio.com
  </div>
</section>
<div class="abs contact-deep"></div>

<section class="abs query">
  <h2>Any Query ? Let's Talk</h2>
  <div class="field" style="left:71px;top:110px;width:465px;height:40px">Full Name</div>
  <div class="field" style="left:71px;top:168px;width:465px;height:40px">Email Address</div>
  <div class="field" style="left:71px;top:226px;width:465px;height:40px">Phone Number</div>
  <div class="field" style="left:568px;top:105px;width:465px;height:157px">Your Message</div>
  <div class="btn">Submit</div>
</section>

<p class="abs footer">Copyright © Willowgate Studio | All Rights Reserved</p>
<div class="abs pay"><div class="pill">Pay Online</div><div class="cards"><span></span><span></span><span></span><span></span></div></div>

</body>
</html>
```